Business Card for a Jewellery Brand

Business card for an upscale jewellery brand. Attached is the brand logo and icon and color board. I am looking for two card versions: one for the founder and one is generic. The card should be elegant and convey upscale and premium feel. I am open to both square and rectangle card shapes.

Industry/Entity Type

Jewelry

Contact Information for Business Card

Two cards: (1) Sunila Perumbadi (Founder) (2) General
(1) Sunila Perumbadi card should have Name: Sunila Perumbadi, Title: Founder Email id: sunila@quelm.com.au. Phone no: +61412555307
(2) Generic card should have Email id: info@quelm.com.au. Phone no: +61431555962

Requirements
Must have
• Workmark
• ICON
• Phone no
• Email ID
• ABN: 48917205563 (Note: ABN is Business number in Australia)
• Website: www.quelm.com.au
• Instagram: quelm_jewellery
• Facebook: @quelmjewellery
Nice to have
• Tagline

```html
<!DOCTYPE html>
<html lang="en">
<head>
<meta charset="utf-8">
<title>QUELM Business Cards</title>
<link rel="stylesheet" href="https://fonts.googleapis.com/css2?family=Jost:wght@400;500&display=swap">
<style>
  :root {
    --backdrop: #4a4a4c;
    --card: #1f1e1f;
    --rose: #e8968f;
    --white: #f4f1f0;
  }
  * { box-sizing: border-box; margin: 0; padding: 0; }
  html, body { width: 1200px; height: 900px; overflow: hidden; }
  body {
    background: var(--backdrop);
    font-family: "Jost", "Futura", sans-serif;
    position: relative;
  }
  .card {
    position: absolute;
    width: 700px;
    height: 400px;
    background: var(--card);
    border-radius: 22px;
    overflow: hidden;
  }
  /* Logo side */
  .card-brand { left: 440px; top: 40px; }
  .brand-lockup {
    position: absolute;
    inset: 0;
    display: flex;
    align-items: center;
    justify-content: center;
    gap: 22px;
  }
  .brand-square {
    width: 26px; height: 26px;
    background: var(--rose);
  }
  .wordmark {
    color: var(--rose);
    font-weight: 400;
    letter-spacing: 0.32em;
    line-height: 1;
  }
  .card-brand .wordmark { font-size: 66px; }

  /* Details side */
  .card-founder { left: 60px; top: 480px; }
  .card-founder .wordmark {
    position: absolute; left: 44px; top: 34px;
    font-size: 54px;
  }
  .edge-tick {
    position: absolute; left: 0; top: 140px;
    width: 5px; height: 28px;
    background: var(--rose);
  }
  .person { position: absolute; left: 56px; top: 144px; }
  .person-name {
    color: var(--rose);
    font-size: 20px;
    letter-spacing: 0.06em;
    text-transform: uppercase;
  }
  .person-title {
    color: var(--white);
    font-size: 15px;
    letter-spacing: 0.06em;
    text-transform: uppercase;
    margin-top: -2px;
  }
  .divider {
    position: absolute; left: 300px; top: 188px;
    width: 350px; height: 2px;
    background: var(--white);
  }
  .contact-list {
    position: absolute; left: 56px; top: 210px;
    list-style: none;
    color: var(--white);
    font-size: 17px;
    letter-spacing: 0.06em;
  }
  .contact-list li {
    display: flex; align-items: center; gap: 14px;
    height: 28px;
  }
  .contact-list svg { width: 16px; height: 16px; flex: none; }
  .accent { color: var(--rose); }
  .abn {
    position: absolute; right: 48px; top: 120px;
    color: var(--white);
    font-size: 17px;
    letter-spacing: 0.08em;
  }
  .abn .label { color: var(--rose); }
  .social {
    position: absolute; right: 60px; top: 240px;
    color: var(--white);
    font-size: 19px;
    letter-spacing: 0.06em;
    line-height: 1.45;
  }
  .social .label { color: var(--rose); }
  .base-band { position: absolute; left: 0; bottom: 0; width: 700px; height: 80px; }
</style>
</head>
<body>

  <section class="card card-brand">
    <div class="brand-lockup">
      <span class="brand-square"></span>
      <span class="wordmark">QUELM</span>
    </div>
  </section>

  <section class="card card-founder">
    <span class="wordmark">QUELM</span>
    <span class="edge-tick"></span>

    <div class="person">
      <p class="person-name">Sunila Perumbadi</p>
      <p class="person-title">Founder</p>
    </div>
    <span class="divider"></span>

    <ul class="contact-list">
      <li>
        <svg viewBox="0 0 16 16"><rect x="4" y="1" width="8" height="14" rx="1.5" fill="none" stroke="var(--white)" stroke-width="1.5"/></svg>
        +61412555307
      </li>
      <li>
        <svg viewBox="0 0 16 16"><rect x="1" y="3" width="14" height="10" fill="var(--white)"/><path d="M1 3 L8 9 L15 3" fill="none" stroke="var(--card)" stroke-width="1.5"/></svg>
        www.<span class="accent">quelm</span>.com.au
      </li>
      <li>
        <svg viewBox="0 0 16 16"><circle cx="7" cy="7" r="5" fill="none" stroke="var(--rose)" stroke-width="2"/><path d="M10.5 10.5 L15 15" stroke="var(--rose)" stroke-width="2"/></svg>
        sunila@quelm.com.au
      </li>
    </ul>

    <p class="abn"><span class="label">ABN:</span> 48917205563</p>

    <div class="social">
      <p><span class="label">Ins:</span> quelm_jewellery</p>
      <p><span class="label">Fb:</span> @quelmjewellery</p>
    </div>

    <svg class="base-band" viewBox="0 0 700 80" aria-hidden="true">
      <path d="M0 8 L440 8 Q452 8 458 20 L462 28" fill="none" stroke="var(--rose)" stroke-width="4"/>
      <path d="M0 28 L450 28 Q470 28 478 18 Q486 8 506 8 L700 8 L700 80 L0 80 Z" fill="var(--rose)"/>
    </svg>
  </section>

</body>
</html>
```